KPV Construction we build lodges in Botswana

We need a Design Layout only with Categories where we can update each projects photos.... We have a web address and a host - kpv.construction

```html
<!DOCTYPE html>
<html lang="en">
<head>
<meta charset="utf-8">
<title>KPV Construction</title>
<link rel="stylesheet" href="https://fonts.googleapis.com/css2?family=Open+Sans:wght@400;600;700&family=Varela+Round&display=swap">
<style>
  :root {
    --ink: #1b1b1b;
    --text: #555555;
    --muted: #9a9a9a;
    --ghost: #ececec;
    --paper: #ffffff;
    --dark: #2b2b2b;
    --darker: #161616;
    --green: #8cc63f;
    --red: #d9352b;
  }
  * { box-sizing: border-box; margin: 0; padding: 0; }
  html, body { width: 1200px; height: 3548px; overflow: hidden; }
  body { position: relative; background: var(--paper); font-family: "Open Sans", sans-serif; color: var(--text); }
  .abs { position: absolute; }
  .heading { font-family: "Varela Round", sans-serif; color: var(--ink); font-weight: 400; }

  /* header */
  .site-header { position: absolute; left: 0; top: 0; width: 1200px; height: 76px; z-index: 3; }
  .brand { position: absolute; left: 108px; top: 0; display: flex; align-items: center; gap: 14px; }
  .brand-mark { width: 40px; height: 60px; background: var(--darker); }
  .brand-name { font-family: "Varela Round", sans-serif; font-size: 22px; color: var(--ink); }
  .main-nav { position: absolute; right: 105px; top: 46px; display: flex; gap: 30px; font-size: 13px; color: var(--ink); }
  .main-nav .active { border-bottom: 2px solid var(--ink); padding-bottom: 4px; }

  /* hero */
  .hero-photo { left: 0; top: 0; width: 1200px; height: 700px;
    background: linear-gradient(180deg, #f4f2ee 0%, #e3dfd8 45%, #bdb6ab 70%, #3a3a3a 88%, #111 100%); }
  .hero-title { left: 0; width: 1200px; top: 218px; text-align: center; font-size: 44px; }
  .hero-sub { left: 350px; width: 500px; top: 276px; text-align: center; font-size: 15px; line-height: 24px; color: #444; }
  .btn { display: inline-block; background: var(--darker); color: #fff; font-size: 13px; font-weight: 600; letter-spacing: 1px; border-radius: 22px; padding: 12px 30px; }
  .hero-btn { left: 527px; top: 354px; }

  /* ghost titles */
  .ghost { position: absolute; font-family: "Varela Round", sans-serif; color: var(--ghost); font-size: 70px; letter-spacing: 4px; text-transform: uppercase; }
  .ghost-num { position: absolute; right: 108px; font-family: "Varela Round", sans-serif; color: var(--ghost); font-size: 84px; }
  .section-title { position: absolute; left: 0; width: 1200px; text-align: center; font-size: 44px; }
  .rule { position: absolute; left: 585px; width: 30px; height: 2px; background: var(--ink); }

  .follow { left: 18px; top: 770px; width: 30px; display: flex; flex-direction: column; align-items: center; gap: 10px; }
  .follow span { width: 10px; height: 10px; border-radius: 50%; background: #bbb; }
  .follow p { writing-mode: vertical-rl; transform: rotate(180deg); font-size: 9px; letter-spacing: 2px; color: var(--muted); }

  .welcome-text { left: 340px; width: 520px; top: 860px; text-align: center; font-size: 13px; line-height: 23px; color: var(--muted); }
  .welcome-btn { left: 504px; top: 1052px; }

  /* works */
  .photo { position: absolute; }
  .project-card { left: 404px; top: 1308px; width: 376px; height: 292px; background: #3a3a3a; border: 10px solid var(--paper); box-shadow: 0 10px 30px rgba(0,0,0,.35); color: #fff; text-align: center; padding: 60px 40px 0; }
  .project-card h3 { font-family: "Varela Round", sans-serif; font-weight: 400; font-size: 24px; letter-spacing: 1px; margin-bottom: 22px; }
  .project-card p { font-size: 13px; line-height: 21px; color: #ddd; }
  .works-arrows { left: 560px; top: 1858px; display: flex; gap: 30px; }

  /* blog */
  .blog-title { left: 614px; top: 2236px; width: 420px; font-family: "Open Sans", sans-serif; font-weight: 700; font-size: 24px; line-height: 32px; color: var(--ink); }
  .blog-meta { left: 614px; top: 2322px; display: flex; gap: 28px; font-size: 12px; color: var(--text); align-items: center; }
  .blog-meta span { display: flex; align-items: center; gap: 8px; }
  .blog-text { left: 614px; top: 2366px; width: 430px; font-size: 13px; line-height: 22px; color: var(--muted); }
  .blog-btn { left: 614px; top: 2560px; }

  /* map + contact */
  .map { left: 0; top: 2700px; width: 1200px; height: 400px; background: linear-gradient(135deg, #ececec 0%, #e2e2e2 50%, #ededed 100%); }
  .contact-bar { left: 224px; top: 3040px; width: 752px; height: 96px; display: flex; box-shadow: 0 8px 24px rgba(0,0,0,.12); }
  .contact-item { flex: 1; display: flex; align-items: center; gap: 14px; padding: 0 34px; background: var(--paper); font-size: 13px; color: var(--ink); line-height: 19px; }
  .contact-item.accent { background: var(--green); color: #fff; }

  .social { left: 0; width: 1200px; top: 3210px; display: flex; justify-content: center; gap: 18px; }
  .social span { width: 40px; height: 40px; border-radius: 50%; border: 2px solid var(--ink); }

  /* footer */
  .footer-line { left: 0; top: 3346px; width: 1200px; height: 1px; background: #ddd; }
  .footer-brand { left: 150px; top: 3386px; width: 46px; height: 70px; background: var(--darker); }
  .footer-nav { right: 108px; top: 3436px; display: flex; gap: 30px; font-size: 13px; color: var(--ink); }
  .copyright { right: 108px; top: 3480px; font-size: 12px; color: var(--muted); }
</style>
</head>
<body>

<header class="site-header">
  <div class="brand"><div class="brand-mark"></div><span class="brand-name">KPV construction</span></div>
  <nav class="main-nav"><span class="active">Home</span><span>About Us</span><span>Services</span><span>Blog</span><span>Contact Us</span></nav>
</header>

<section class="hero">
  <div class="abs hero-photo" role="img" aria-label="Lodge under construction in timber scaffolding, with a silhouette of workers, acacia trees and elephants along the bottom"></div>
  <svg class="abs" style="left:0;top:660px" width="1200" height="110" viewBox="0 0 1200 110">
    <path d="M0 40 Q600 160 1200 40 L1200 0 L0 0 Z" fill="#111"/>
    <path d="M0 40 Q600 160 1200 40 L1200 110 L0 110 Z" fill="#fff"/>
    <path d="M588 88 L600 98 L612 88" fill="none" stroke="#fff" stroke-width="3"/>
  </svg>
  <h1 class="abs heading hero-title">KPV construction</h1>
  <p class="abs hero-sub">We are a Construction Company based in the Okavango Delta and specialize in Lodge building...</p>
  <span class="abs btn hero-btn">GET STARTED</span>
</section>

<section class="welcome">
  <div class="ghost" style="left:410px;top:722px">Welcome</div>
  <div class="ghost-num" style="top:728px">01</div>
  <div class="abs follow"><span></span><span></span><span></span><p>FOLLOW US</p></div>
  <h2 class="heading section-title" style="top:766px">KPV construction</h2>
  <div class="rule" style="top:836px"></div>
  <p class="abs welcome-text">We design and build lodges, camps and guest houses across Botswana, from the Okavango Delta to the Kalahari. Our team handles every stage of the work, from the first site visit and plans to the final handover. We use local timber, thatch and stone, and we work with care for the land and the wildlife around each site. Browse our projects below to see the lodges we have completed.</p>
  <span class="abs btn welcome-btn">READ MORE</span>
</section>

<section class="works">
  <div class="ghost" style="left:430px;top:1158px">Projects</div>
  <div class="ghost-num" style="top:1164px">02</div>
  <h2 class="heading section-title" style="top:1188px">Our Works</h2>
  <div class="rule" style="top:1256px"></div>
  <svg class="abs" style="left:0;top:1270px" width="1200" height="730" viewBox="0 0 1200 730">
    <path d="M0 60 Q300 0 600 40 Q900 80 1200 20 L1200 650 Q900 730 600 680 Q300 630 0 700 Z" fill="#2b2b2b"/>
  </svg>
  <div class="photo" style="left:108px;top:1332px;width:286px;height:228px;background:linear-gradient(160deg,#6f7f5a,#3e4a33)" role="img" aria-label="Thatched gazebo among trees"></div>
  <div class="photo" style="left:790px;top:1332px;width:298px;height:228px;background:linear-gradient(160deg,#5d6b5a,#2c342b)" role="img" aria-label="Lodge clearing at dusk"></div>
  <div class="photo" style="left:108px;top:1592px;width:312px;height:232px;background:linear-gradient(170deg,#9ec4e8,#6f8f4a 70%,#8a7a5a)" role="img" aria-label="Thatched shelter on a lawn"></div>
  <div class="photo" style="left:432px;top:1592px;width:348px;height:232px;background:linear-gradient(170deg,#a9cdea,#6d9a3e 65%,#5e7f33)" role="img" aria-label="Grass field with thatched huts"></div>
  <div class="photo" style="left:780px;top:1592px;width:308px;height:232px;background:linear-gradient(160deg,#b7d3ec,#c2884a 55%,#7a5230)" role="img" aria-label="Timber frame lodge being built"></div>
  <div class="abs project-card">
    <h3>PROJECT NAME</h3>
    <p>A thatched safari lodge with six guest rooms, built on raised timber decks at the edge of the river.</p>
  </div>
  <svg class="abs works-arrows" width="80" height="30" viewBox="0 0 80 30">
    <path d="M20 5 L10 15 L20 25" fill="none" stroke="#aaa" stroke-width="3"/>
    <path d="M60 5 L70 15 L60 25" fill="none" stroke="#aaa" stroke-width="3"/>
  </svg>
</section>

<section class="blog">
  <div class="ghost" style="left:360px;top:2034px">Latest Post</div>
  <div class="ghost-num" style="top:2040px">03</div>
  <h2 class="heading section-title" style="top:2066px">Our Blog</h2>
  <div class="rule" style="top:2134px"></div>
  <div class="photo" style="left:132px;top:2192px;width:316px;height:480px;background:linear-gradient(170deg,#cfe3f2,#a4653a 45%,#6e9b3c 80%,#5b8a2e)" role="img" aria-label="Timber cabin with green garden, cut in the shape of a map outline"></div>
  <h3 class="abs blog-title">SED UT PERSPICIATIS UNDE OMNIS ISTE NATUS</h3>
  <div class="abs blog-meta">
    <span><svg width="12" height="12" viewBox="0 0 12 12"><circle cx="6" cy="3.5" r="2.8" fill="#333"/><path d="M0.5 12 Q6 4 11.5 12 Z" fill="#333"/></svg>By Author Name</span>
    <span><svg width="12" height="12" viewBox="0 0 12 12"><rect x="1" y="2" width="10" height="9" fill="none" stroke="#333" stroke-width="1.5"/><line x1="1" y1="5" x2="11" y2="5" stroke="#333" stroke-width="1.5"/></svg>03-01-2019</span>
  </div>
  <p class="abs blog-text">Every lodge starts with the site. Before we draw a single plan, we walk the land with our clients, study the water levels and the paths the animals use, and choose where each room can face the best view. This careful start saves time later and gives each lodge its own calm character in the bush.</p>
  <span class="abs btn blog-btn">READ MORE</span>
</section>

<section class="contact">
  <div class="abs map" role="img" aria-label="Street map around the office location"></div>
  <div class="abs contact-bar">
    <div class="contact-item">
      <svg width="18" height="24" viewBox="0 0 18 24"><path d="M9 0 C4 0 0 4 0 9 C0 15 9 24 9 24 C9 24 18 15 18 9 C18 4 14 0 9 0 Z" fill="#1b1b1b"/><circle cx="9" cy="9" r="3.5" fill="#fff"/></svg>
      <span>14 Acacia Road,<br>Maun</span>
    </div>
    <div class="contact-item accent">
      <svg width="22" height="16" viewBox="0 0 22 16"><rect x="1" y="1" width="20" height="14" fill="none" stroke="#fff" stroke-width="2"/><path d="M1 1 L11 9 L21 1" fill="none" stroke="#fff" stroke-width="2"/></svg>
      <span>hello@kpv.construction</span>
    </div>
    <div class="contact-item">
      <svg width="20" height="20" viewBox="0 0 20 20"><path d="M4 1 L8 5 L6 8 Q8 12 12 14 L15 12 L19 16 L16 19 Q6 18 1 4 Z" fill="#1b1b1b"/></svg>
      <span>+267 555 0142</span>
    </div>
  </div>
  <div class="abs social" aria-label="Social network links"><span></span><span></span><span></span><span></span><span></span></div>
</section>

<footer>
  <div class="abs footer-line"></div>
  <div class="abs footer-brand" aria-label="KPV construction"></div>
  <nav class="abs footer-nav"><span>Home</span><span>About Us</span><span>Projects</span><span>Blog</span><span>Contact Us</span></nav>
  <p class="abs copyright">Copyright © Your Website 2019</p>
</footer>

</body>
</html>
```